Mosswood Chiropractic Web Design

We need a fully operating Web site design INCLUDING the code for a Chiropractic Clinic based in Auckland New Zealand to target people from different financial backgrounds.

We need 4 Pages as followed:
1. Home: includes Slideshow of the clinic, General information about chiropractic, option for "Request an appointment", and it would be nice to have a picture on the top right side of the header and the clinic's name and logo on the top left side. on the bottom right we would like a small section for "Testimonial" (A good example: http://www.fernlightstudio.example/ )
(A good example for slide show is: http://www.bektora.example.nz/)
(A good example for the header is: http://www.spinewellpraxis.example/)

2. About Us: this section will include the background information of the company, and a section for our staff (which will includes a photo and description of each person/staff which can be changedanytime)
(a good example: http://www.harbourlanechiro.example.nz/)

3. Contact: includes location, map, contact numbers, email, and a contact box (A good example: http://www.fernlightstudio.example/contact/)

4. Services: includes our products, adjustment equipment, chiropractic products for sale, few pictures of patients while under chiropractic care/adjustment tables

We would also like to add "social networking" options on the bottom left side of every page (Facebook, twitter, Blog, Google+)

Please check the following links to get a feel of our favorite designs:
http://www.spinewellpraxis.example/
http://www.harbourlanechiro.example.nz/
http://www.bektora.example.nz/
http://www.brindlechiropracticclinic.example/
http://www.stillwoven.example.nz/
http://www.pqr.example.nz/index-1.html
http://home.keelbrookchiro.example.nz/home/

we would like to have full access to the back-end- admin of the website to be able to change and add any pictures or texts.
Updates

Hi Lovely Designer,

thank you so much for your proposed designs. We just uploaded the original source file of our logo, for you all to have access on it to facilitate your work. 

Enjoy your day

Orla

Target Market(s)

People with different financial background as well as we are located in the artistic part of town, so appealing to those crowd is important to us.

Industry/Entity Type

Financial

Requirements
Must have
• 1.color similar to the logo or darker colors (Dark and rich colors are prefered)
2. more artistic than a basic doctors' clinic
3. I would like the opening of the web to bring art, tranquility and peaceful images into mind
Should not have
• Not bombarded with lots of info and pics in one page, not too busy and crowded

```html
<!DOCTYPE html>
<html lang="en">
<head>
<meta charset="utf-8">
<title>Mosswood Chiropractic</title>
<link rel="stylesheet" href="https://fonts.googleapis.com/css2?family=Dosis:wght@400;500;600&family=Ubuntu:ital,wght@0,400;0,500;0,700;1,400;1,700&display=swap">
<style>
:root{
  --blue-deep:#0b3a73;
  --blue-mid:#195a9c;
  --blue-light:#2a6fb4;
  --footer:#0a2e5a;
  --lime:#8cc63f;
  --lime-dark:#5e9a12;
  --white:#ffffff;
  --text:#e6eef8;
  --muted:#c9d6e6;
  --btn:#0a2a52;
  --star:#f4811f;
  --date:#b4e03c;
}
*{margin:0;padding:0;box-sizing:border-box}
html,body{width:993px;height:1200px;overflow:hidden}
body{
  position:relative;
  background:radial-gradient(ellipse 70% 55% at 50% 35%,var(--blue-light) 0%,var(--blue-mid) 45%,var(--blue-deep) 100%);
  font-family:'Ubuntu',sans-serif;color:var(--text);
}
.abs{position:absolute}
.brand{left:0;width:993px;top:30px;text-align:center;font-family:'Dosis',sans-serif;font-weight:500;font-size:30px;color:var(--lime);letter-spacing:1px}
.brand-sub{left:0;width:993px;top:72px;text-align:center;font-family:'Dosis',sans-serif;font-weight:500;font-size:14px;letter-spacing:4px;color:var(--lime)}
.nav a{position:absolute;top:127px;height:39px;line-height:39px;font-family:'Dosis',sans-serif;font-size:17px;color:var(--white);text-decoration:none}
.nav .active{left:219px;width:96px;text-align:center;background:linear-gradient(var(--lime),#6aaa1c)}
.hero{left:98px;top:180px;width:797px;height:327px;background:var(--white);box-shadow:0 10px 18px rgba(0,0,0,.35);padding:6px}
.hero-photo{width:100%;height:100%;background:linear-gradient(100deg,#e9ecef 0%,#b8c9d6 35%,#8fc2d6 55%,#c9d9b0 80%,#eef0e4 100%)}
.intro-brand{left:95px;top:546px;font-family:'Dosis',sans-serif;font-weight:500;font-size:26px;color:var(--white);display:flex;align-items:center;gap:10px}
.intro-brand .dot{width:14px;height:14px;border-radius:50%;background:var(--white)}
.appt{left:669px;top:532px;width:224px;height:64px;border:2px solid var(--white);border-radius:6px;background:linear-gradient(#a6d94a,#6fb21c);box-shadow:0 3px 8px rgba(0,0,0,.35)}
.appt .small{position:absolute;left:20px;top:12px;font-family:'Dosis',sans-serif;font-size:14px;color:var(--white)}
.appt .big{position:absolute;left:16px;top:26px;font-family:'Dosis',sans-serif;font-weight:600;font-size:22px;color:#184a05}
.appt svg{position:absolute;right:2px;top:2px}
.dotted{border-top:1px dotted rgba(255,255,255,.45)}
.framed{background:var(--white);padding:6px;box-shadow:0 4px 10px rgba(0,0,0,.3)}
.ph{width:100%;height:100%}
.intro-img{left:98px;top:631px;width:171px;height:152px}
.intro-text{left:297px;top:628px;width:587px;font-size:10.6px;line-height:16.5px}
.intro-text p+p{margin-top:16px}
.intro-text b{font-style:italic}
.more{display:block;position:absolute;background:var(--btn);color:var(--white);font-size:9.5px;font-weight:700;font-style:italic;text-align:center;text-decoration:none}
.rule{left:98px;width:797px;height:1px;background:linear-gradient(90deg,transparent,rgba(255,255,255,.35),transparent)}
.col-title{top:832px;font-weight:700;font-size:15px;color:var(--white)}
.col-text{top:987px;width:220px;font-size:10.6px;line-height:16.7px;text-align:justify}
.testi h3{font-weight:500;font-size:13px;color:var(--white)}
.testi .date{font-size:8.5px;font-style:italic;color:var(--date)}
.testi p{font-size:9.6px;line-height:15px;color:var(--white)}
.footer{left:0;top:1115px;width:993px;height:85px;background:var(--footer)}
.vline{top:1130px;width:1px;height:60px;background:rgba(255,255,255,.15)}
.f-title{font-family:'Dosis',sans-serif;font-weight:600;font-size:14px;color:#d6e0ec}
.social span{position:absolute;top:1159px;width:27px;height:27px;border-radius:50%;border:2px solid #d9e2ee}
.f-links{left:293px;width:381px;top:1143px;text-align:center;font-size:10px;color:var(--muted);line-height:20px}
.email{left:713px;top:1160px;font-family:'Dosis',sans-serif;font-weight:600;font-size:14px;color:var(--white)}
</style>
</head>
<body>
<div class="abs brand">MOSSWOOD</div>
<div class="abs brand-sub">CHIROPRACTIC</div>

<nav class="nav">
  <a class="active" href="#">Home</a>
  <a style="left:340px" href="#">About Us</a>
  <a style="left:461px" href="#">Services</a>
  <a style="left:574px" href="#">Testimonials</a>
  <a style="left:717px" href="#">Contact Us</a>
</nav>

<div class="abs hero"><div class="hero-photo" role="img" aria-label="Slideshow photo of a smiling mother giving her daughter a piggyback ride outdoors"></div></div>

<div class="abs intro-brand"><span class="dot"></span>Mosswood Chiropractic</div>

<a class="abs appt" href="#">
  <span class="small">Click Here to Make an</span>
  <span class="big">APPOINTMENT</span>
  <svg width="56" height="56" viewBox="0 0 56 56"><circle cx="28" cy="28" r="25" fill="#fff" stroke="#9aa7b4" stroke-width="3"/><line x1="28" y1="28" x2="28" y2="10" stroke="#222" stroke-width="2"/><line x1="28" y1="28" x2="42" y2="36" stroke="#1a3f9a" stroke-width="1.5"/></svg>
</a>

<div class="abs dotted" style="left:298px;top:612px;width:581px"></div>

<div class="abs intro-img framed"><div class="ph" role="img" aria-label="Woman's back with highlighted spine over an x-ray background" style="background:linear-gradient(135deg,#5fb3d3,#2a86b0 50%,#a9dbea)"></div></div>
<div class="abs intro-text">
  <p><b>Lorem ipsum dolor sit amet, consectetuer adipiscing elit. Nam cursus. Morbi ut mi. Nullam enim leo, egestas</b> id, condimentum at, laoreet mattis, massa. Sed eleifend nonummy diam. Praesent mauris ante, elementum et, bibendum at, posuere sit amet, nibh. Duis tincidunt lectus quis dui viverra vestibulum. Suspendisse vulputate aliquam dui. Nulla elementum dui ut augue. Aliquam vehicula mi at mauris.</p>
  <p>Morbi magna magna, tincidunt a, mattis non, imperdiet vitae, tellus. Sed odio est, auctor ac, sollicitudin in, consequat vitae, orci. Fusce id felis. Vivamus sollicitudin metus eget eros.</p>
</div>
<a class="more" style="left:296px;top:756px;width:79px;height:27px;line-height:27px" href="#">Read More</a>

<div class="abs rule" style="top:809px"></div>

<h2 class="abs col-title" style="left:128px">Personal Chiropractic Care</h2>
<div class="abs" style="left:109px;top:883px;width:219px;height:88px" role="img" aria-label="Hands massaging a patient's shoulder"><div class="ph" style="background:linear-gradient(90deg,#c9b7a8,#e9dfd6 50%,#d8ccc3)"></div></div>
<p class="abs col-text" style="left:108px">Pellentesque habitant morbi tristique senectus et netus et malesuada fames ac turpis egestas. In posuere felis nec tortor.</p>
<a class="more" style="left:110px;top:1046px;width:79px;height:27px;line-height:27px" href="#">Read More</a>

<h2 class="abs col-title" style="left:411px">Corporate Chiropractic</h2>
<div class="abs framed" style="left:385px;top:878px;width:230px;height:99px"><div class="ph" role="img" aria-label="Doctor explaining a spine model to a patient" style="background:linear-gradient(90deg,#9bb3c6,#e6edf2 45%,#b9c7d2)"></div></div>
<p class="abs col-text" style="left:390px">Pellentesque habitant morbi tristique senectus et netus et malesuada fames ac turpis egestas. In posuere felis nec tortor.</p>
<a class="more" style="left:390px;top:1049px;width:80px;height:28px;line-height:28px" href="#">Read More</a>

<h2 class="abs col-title" style="left:671px">Recent Testimonials</h2>
<div class="abs testi" style="left:676px;top:872px;width:211px">
  <h3>Thanks for the treatment</h3>
  <svg width="72" height="14" viewBox="0 0 72 14" style="margin-top:4px"><g fill="var(--star)"><polygon id="st" points="7,0 9,5 14,5 10,8 11.5,13.5 7,10.2 2.5,13.5 4,8 0,5 5,5"/><use href="#st" x="14"/><use href="#st" x="28"/><use href="#st" x="42"/><use href="#st" x="56"/></g></svg>
  <div class="date">May 12, 2013 by Taren</div>
  <p>Pellentesque habitant morbi tristique senectus et netus...</p>
  <div class="dotted" style="margin:6px 0 9px"></div>
  <h3>Ut accumsan ultricies elit</h3>
  <svg width="72" height="14" viewBox="0 0 72 14" style="margin-top:3px"><g fill="var(--star)"><use href="#st"/><use href="#st" x="14"/><use href="#st" x="28"/><use href="#st" x="42"/><use href="#st" x="56"/></g></svg>
  <div class="date">May 12, 2013 by Taren</div>
  <p>Pellentesque habitant morbi tristique senectus et netus...</p>
</div>

<div class="abs rule" style="top:1089px"></div>

<footer class="abs footer"></footer>
<div class="abs f-title" style="left:94px;top:1134px">Get Connected</div>
<div class="social">
  <span style="left:87px"></span><span style="left:120px"></span><span style="left:153px"></span><span style="left:186px"></span><span style="left:220px"></span>
</div>
<div class="abs vline" style="left:293px"></div>
<div class="abs f-links">Home &nbsp;|&nbsp; About Us &nbsp;|&nbsp; Services &nbsp;|&nbsp; Testimonials &nbsp;|&nbsp; Contact Us<br>Mosswood Chiropractic , Copy Right &nbsp;&nbsp;&nbsp;&nbsp;2013</div>
<div class="abs vline" style="left:674px"></div>
<div class="abs f-title" style="left:713px;top:1138px">Contact Us @</div>
<div class="abs email">info@mosswoodchiropractic.example</div>
</body>
</html>
```